Verbena Home- Hang tags for Modern Handmade Home Decor products

We need to design some hang tags to use for our products, we want double tags, meaning two tags that go together on one string, two different and coordinating sizes and shapes. We have a logo, what we need is the artwork for these two tags to take to print. One tag will have the logo on one side and company information on the other, the second tag will be for product information. For example, we specialize in handmade pieces from Latin America, on the product tag I want space to write the product info but also a line for what country it's from and what community created it. I'm attaching an image of the shapes of tags that I like, along with a copy of our logo. On the larger company tag I'd like our logo in the center and a color block stripe of the yellow color of our logo at the bottom, on the flip side there will just be text, sort of our company motto. On the narrower longer product info tag I'd like a small logo at the bottom end and space for product information to be written in by hand and on the flip side of this one lines for what country it's from, what community created it and care instructions, again, all information that we will write in by hand. Please let me know if you have questions.

Target Market(s)

Design savvy, house proud, well educated people who travel and appreciate art.

Font styles to use
Sans Serif

Requirements
Must have
• I want it to look graphic, sophisticated and modern. I want to be very legible and clean.
Nice to have
• Clarity, easy to read, and maybe a bit of whimsy or lightheartedness.
Should not have
• Nothing that feels "ethnic" or "crafty:, even though our products are handmade in Latin America they are contemporary and sophisticated, not stereotypical.

```html
<!DOCTYPE html>
<html lang="en">
<head>
<meta charset="utf-8">
<title>Verbena Home – Product Hang Tag</title>
<link href="https://fonts.googleapis.com/css2?family=Poppins:wght@300&family=Mrs+Saint+Delafield&family=Mr+Dafoe&display=swap" rel="stylesheet">
<style>
  :root {
    --backdrop: #b2b2b2;
    --tag-paper: #e7e7e7;
    --brand-yellow: #fccf05;
    --brand-ink: #efefef;
    --script-ink: #111111;
    --divider: #f3f3f3;
  }
  html, body {
    margin: 0;
    padding: 0;
    width: 1200px;
    height: 1000px;
    overflow: hidden;
    background: var(--backdrop);
  }
  .canvas {
    position: relative;
    width: 1200px;
    height: 1000px;
  }
  .tag-shape {
    position: absolute;
    left: 0;
    top: 0;
  }
  .brand-name,
  .brand-web {
    position: absolute;
    left: 453px;
    width: 294px;
    margin: 0;
    text-align: center;
    white-space: nowrap;
    font-family: "Poppins", sans-serif;
    font-weight: 300;
    color: var(--brand-ink);
    line-height: 1;
  }
  .brand-name {
    top: 274px;
    font-size: 38px;
    letter-spacing: 0.5px;
  }
  .brand-web {
    top: 326px;
    font-size: 10px;
    letter-spacing: 3px;
  }
  .origin-message {
    position: absolute;
    left: 385px;
    top: 0;
    width: 430px;
    height: 1000px;
    margin: 0;
    color: var(--script-ink);
  }
  .origin-message .line {
    position: absolute;
    left: 0;
    width: 430px;
    text-align: center;
    white-space: nowrap;
    font-family: "Mrs Saint Delafield", cursive;
    line-height: 1;
  }
  .line-lead { top: 455px; font-size: 62px; letter-spacing: 5px; }
  .line-middle { top: 560px; font-size: 40px; letter-spacing: 4px; }
  .line-from { top: 650px; font-size: 42px; letter-spacing: 3px; }
  .origin-message .line-region {
    top: 728px;
    font-family: "Mr Dafoe", cursive;
    font-size: 58px;
    letter-spacing: 0;
  }
</style>
</head>
<body>
<main class="canvas">
  <svg class="tag-shape" width="1200" height="1000" viewBox="0 0 1200 1000" aria-hidden="true">
    <defs>
      <filter id="tag-shadow" x="-20%" y="-20%" width="140%" height="140%">
        <feDropShadow dx="0" dy="2" stdDeviation="5" flood-color="#000" flood-opacity="0.35"/>
      </filter>
      <filter id="band-shadow" x="-20%" y="-20%" width="140%" height="140%">
        <feDropShadow dx="0" dy="2" stdDeviation="3" flood-color="#000" flood-opacity="0.2"/>
      </filter>
    </defs>
    <polygon class="tag-body" points="385,78 815,78 815,840 600,920 385,840" fill="var(--tag-paper)" filter="url(#tag-shadow)"/>
    <polygon class="brand-band" points="453,90 747,90 747,330 600,415 453,330" fill="var(--brand-yellow)" filter="url(#band-shadow)"/>
    <circle class="string-hole" cx="600" cy="106" r="10" fill="#ffffff"/>
    <line class="band-divider" x1="460" y1="422" x2="745" y2="422" stroke="var(--divider)" stroke-width="2"/>
  </svg>

  <p class="brand-name">verbena home</p>
  <p class="brand-web">www.verbenahome.com</p>

  <p class="origin-message">
    <span class="line line-lead">This Products</span>
    <span class="line line-middle">are handmade</span>
    <span class="line line-from">from</span>
    <span class="line line-region">Latin America</span>
  </p>
</main>
</body>
</html>
```